Consulting company needs Business Cards - rough concept provided

I'm looking for someone to take our business card idea and make is slick and polished - to communicate our high-end, sophisticated, serious consulting business. We have a rough layout we did in-house. We are open to ideas on repo-ing elements, adjusting sizes, typefaces etc... within the general concept we've already come up with. We want it to be super-clean and sophisticated. We want to keep the white backgrounds, and blue brand colors. Our goal is to print with painted blue edges on thick cardstock. Thank you!!

```html
<!DOCTYPE html>
<html lang="en">
<head>
<meta charset="utf-8">
<title>Northvale Business Card</title>
<link rel="stylesheet" href="https://fonts.googleapis.com/css2?family=Poppins:wght@400;700;800&family=Quicksand:wght@300&display=swap">
<style>
  :root {
    --brand-blue: #0a8bd2;
    --card-white: #f7f7f6;
    --ink-grey: #4a4a4a;
    --muted-grey: #6b6b6b;
    --backdrop: #e4e1de;
  }
  html, body {
    margin: 0;
    padding: 0;
    overflow: hidden;
    background: var(--backdrop);
  }
  .canvas {
    position: relative;
    width: 936px;
    height: 1200px;
    overflow: hidden;
    background: var(--backdrop);
    font-family: "Poppins", sans-serif;
  }
  .card {
    position: absolute;
    left: 88px;
    width: 760px;
    height: 434px;
    box-shadow: 0 6px 18px rgba(0, 0, 0, 0.18);
    overflow: hidden;
  }
  .card--front { top: 140px; background: var(--card-white); }
  .card--back { top: 626px; background: var(--brand-blue); }

  /* front */
  .wordmark {
    position: absolute;
    left: 122px;
    top: 217px;
    transform: translate(-50%, -50%) rotate(-90deg);
    font-weight: 800;
    font-size: 60px;
    line-height: 1;
    letter-spacing: 1px;
    color: var(--brand-blue);
    white-space: nowrap;
  }
  .holder {
    position: absolute;
    right: 52px;
    top: 48px;
    text-align: right;
  }
  .holder__name {
    font-weight: 700;
    font-size: 29px;
    line-height: 1.2;
    color: var(--brand-blue);
  }
  .holder__role {
    font-size: 16px;
    line-height: 1.3;
    color: var(--muted-grey);
  }
  .accent-square {
    position: absolute;
    right: 0;
    top: 61px;
    width: 38px;
    height: 44px;
    background: var(--brand-blue);
  }
  .address {
    position: absolute;
    right: 58px;
    top: 244px;
    text-align: right;
    font-size: 17px;
    line-height: 23px;
    color: var(--ink-grey);
  }
  .contact {
    position: absolute;
    right: 50px;
    top: 310px;
    margin: 0;
    padding: 0;
    list-style: none;
    font-size: 17px;
    line-height: 23px;
    color: var(--ink-grey);
  }
  .contact__item {
    display: flex;
    justify-content: flex-end;
    align-items: center;
    gap: 14px;
  }
  .contact__icon {
    width: 14px;
    height: 14px;
    fill: var(--brand-blue);
  }

  /* back */
  .positioning {
    position: absolute;
    left: 50px;
    top: 66px;
    color: #ffffff;
    white-space: nowrap;
  }
  .positioning__line {
    line-height: 1;
    margin: 0;
  }
  .positioning__key {
    font-family: "Poppins", sans-serif;
    font-weight: 800;
    font-size: 40px;
  }
  .positioning__fill {
    font-family: "Quicksand", sans-serif;
    font-weight: 300;
    font-size: 41px;
  }
  .positioning__line--key { margin-top: 16px; }
  .positioning__line--key:first-child { margin-top: 0; }
  .positioning__line--fill { margin-top: 2px; }
  .positioning__line--inline { margin-top: 20px; }
</style>
</head>
<body>
<main class="canvas">

  <section class="card card--front" aria-label="Card front">
    <div class="wordmark">NORTHVALE</div>

    <div class="holder">
      <div class="holder__name">Dana Whitlock</div>
      <div class="holder__role">Brand Consultant</div>
    </div>
    <div class="accent-square"></div>

    <div class="address">
      4850 Harbor Ave, Ste210<br>
      Lakeview, CA 90417
    </div>

    <ul class="contact">
      <li class="contact__item">
        <span>(555) 014 2290</span>
        <svg class="contact__icon" viewBox="0 0 16 16" aria-hidden="true">
          <path d="M3.6 1.2l2.3 2.6-1.3 2a9 9 0 0 0 5.6 5.6l2-1.3 2.6 2.3-1.4 2.2C8.6 15 1 7.4 1.4 2.6z"/>
        </svg>
      </li>
      <li class="contact__item">
        <span>dana@northvale.com</span>
        <svg class="contact__icon" viewBox="0 0 16 16" aria-hidden="true">
          <path d="M1 3h14v10H1z M2.2 4.2L8 8.6l5.8-4.4" fill="var(--brand-blue)"/>
          <path d="M2 4l6 4.6L14 4" fill="none" stroke="#fff" stroke-width="1.2"/>
        </svg>
      </li>
      <li class="contact__item">
        <span>dana@northvale.com</span>
        <svg class="contact__icon" viewBox="0 0 16 16" aria-hidden="true">
          <circle cx="8" cy="8" r="7"/>
          <path d="M1.5 8h13M8 1c-2.6 3-2.6 11 0 14M8 1c2.6 3 2.6 11 0 14" fill="none" stroke="#fff" stroke-width="1"/>
        </svg>
      </li>
    </ul>
  </section>

  <section class="card card--back" aria-label="Card back">
    <div class="positioning">
      <p class="positioning__line positioning__line--key"><span class="positioning__key">WE HELP</span></p>
      <p class="positioning__line positioning__line--fill"><span class="positioning__fill">[TARGET DEMOGRAPHIC]</span></p>
      <p class="positioning__line positioning__line--key"><span class="positioning__key">ACHIEVE</span></p>
      <p class="positioning__line positioning__line--fill"><span class="positioning__fill">[DESIRED EMOTIONAL OUTCOME]</span></p>
      <p class="positioning__line positioning__line--inline"><span class="positioning__key">BY</span> <span class="positioning__fill">[OUR UNIQUE APPROACH]</span></p>
      <p class="positioning__line positioning__line--inline"><span class="positioning__key">BECAUSE</span> <span class="positioning__fill">[OUR BRAND BELIEFS]</span></p>
    </div>
  </section>

</main>
</body>
</html>
```